Lien Post Card - (5.5 x 8.5)

FRONT OF POSTCARD
Is a Property Lien Putting Your Home at Risk?
HOA Liens • Tax Liens • Municipal Charges • Other Property-Related Liens
You may have options to resolve outstanding liens and protect your home.
A Refinance or Home Equity Line of Credit (HELOC) may help you:
✔ Pay off qualifying liens
✔ Consolidate debt into one manageable payment
✔ Access your home's equity
✔ Improve your financial flexibility
✔ Avoid additional penalties, fees, or collection actions
Don't wait until the situation becomes more difficult.
Call today for a confidential review of your options.
Bluegate Lending Partners, Inc.
(800) 647-2915 x 42
www.bluegatelendco.com
NMLS #381640
BACK OF POSTCARD
Your Home Equity Could Be the Solution
If you have received notices regarding:
• Delinquent Property Taxes
• HOA or Condo Association Assessments
• Municipal Utility Liens
• Special Assessments
• Other Property-Related Obligations
You may qualify for financing options designed to help satisfy those obligations and bring your property current.
Our experienced mortgage professionals can review your situation and discuss available programs, including:
• Cash-Out Refinancing
• Home Equity Lines of Credit (HELOCs)
• Home Equity Loans
• Debt Consolidation Solutions
Free Consultation • No Obligation
Contact Marcus Delaney today at (800) 647-2915 x42 or mdelaney@bluegatelendco.com (NMLS #57308)

```html
<!DOCTYPE html>
<html lang="en">
<head>
<meta charset="utf-8">
<title>Lien Postcard – Bluegate Lending Partners</title>
<link href="https://fonts.googleapis.com/css2?family=Outfit:wght@400;500;600;700;800&family=Roboto:wght@400;500&display=swap" rel="stylesheet">
<style>
  :root{
    --backdrop:#a8a9ad;
    --navy:#0e4c83;
    --navy-deep:#0b4877;
    --green:#a1cd3c;
    --green-text:#8cc63f;
    --blue:#1b9ad8;
    --sky:#2a9fe0;
    --ink:#2b2b2b;
    --grey-text:#3d3d3d;
    --white:#ffffff;
  }
  *{box-sizing:border-box;margin:0;padding:0}
  html,body{width:869px;height:1200px;overflow:hidden}
  body{background:var(--backdrop);font-family:"Outfit",sans-serif;position:relative}

  .card{position:absolute;left:62px;width:745px;height:481px;background:var(--white);overflow:hidden}
  .card--front{top:110px}
  .card--back{top:619px;height:482px}
  .abs{position:absolute}

  /* FRONT */
  .front-haze{left:0;top:0;width:520px;height:189px;background:linear-gradient(90deg,#dfe2e5 0%,#f1f2f3 40%,rgba(255,255,255,0) 100%)}
  .headline{left:38px;top:31px;font-weight:800;font-size:28px;line-height:34px;color:var(--navy);letter-spacing:.1px}
  .headline .accent{color:var(--green-text)}
  .lien-types{left:39px;top:102px;font-size:13.6px;color:var(--ink);white-space:nowrap}
  .rule{left:40px;top:127px;width:57px;height:1.5px;background:var(--navy)}
  .options{left:39px;top:134px;font-size:16.5px;line-height:21px;font-weight:600;color:var(--navy)}

  .green-band{left:0;top:189px;width:560px;height:178px;background:var(--green)}
  .help-title{left:38px;top:203px;font-size:13.6px;line-height:17px;font-weight:600;color:var(--navy)}
  .help-list{left:46px;top:242px;list-style:none;font-family:"Roboto",sans-serif;font-size:12.2px;line-height:14px;color:var(--navy)}
  .help-list li{position:relative;padding-left:16px;margin-bottom:3px}
  .check::before,.help-list li::before,.notice-list li::before{content:"";position:absolute;left:1px;top:3px;width:4px;height:7px;border:solid currentColor;border-width:0 1.8px 1.8px 0;transform:rotate(45deg)}

  .urgent-circle{left:272px;top:200px;width:156px;height:156px;border-radius:50%;background:var(--navy-deep);color:var(--white);padding:30px 0 0 32px;font-weight:600;font-size:15px;line-height:19.5px}

  .photo-circle{left:441px;top:135px;width:272px;height:272px;border-radius:50%;background:radial-gradient(circle at 45% 40%,#e9e6e2 0%,#b9b3ad 45%,#4a5a78 80%,#3b4660 100%);z-index:2}

  .call-band{left:0;top:367px;width:745px;height:114px;background:linear-gradient(90deg,var(--blue) 0%,var(--blue) 50%,#1679b8 70%,#0a3d66 88%,#071f35 100%)}
  .call-text{left:41px;top:383px;font-size:18px;line-height:23px;color:var(--white);text-transform:uppercase}
  .call-text b{font-weight:700}
  .contact-row{left:40px;top:441px;display:flex;align-items:center;color:var(--white);white-space:nowrap}
  .phone-big{font-size:18px;font-weight:600;display:flex;align-items:center;gap:6px}
  .web{font-size:14.5px;margin-left:20px;display:flex;align-items:center;gap:5px}
  .nmls-front{left:644px;top:436px;font-size:13px;color:var(--white);font-weight:500}

  .brand-front{left:600px;top:58px;width:160px;text-align:center;font-size:17px;line-height:20px;font-weight:700;color:var(--navy)}

  /* BACK */
  .back-haze{left:300px;top:0;width:445px;height:250px;background:linear-gradient(90deg,rgba(255,255,255,0) 0%,#e6e7e8 45%,#cfd1d3 100%)}
  .back-headline{left:34px;top:29px;font-weight:800;font-size:25.5px;line-height:29px;color:var(--navy)}
  .notice-lead{left:39px;top:92px;font-size:15.5px;font-weight:600;color:var(--sky)}
  .notice-list{left:46px;top:119px;list-style:none;font-size:12.4px;line-height:15.1px;color:var(--grey-text)}
  .notice-list li{position:relative;padding-left:14px;color:var(--grey-text)}
  .notice-list li::before{color:var(--sky);top:3px}
  .qualify{left:39px;top:205px;font-size:12.6px;line-height:15.5px;color:var(--grey-text)}
  .stamp-box{left:631px;top:35px;width:80px;height:80px;background:var(--white);border:1px solid #d3d4d6}

  .programs-band{left:0;top:250px;width:745px;height:79px;background:var(--blue)}
  .programs-intro{left:0;top:250px;width:285px;height:79px}
  .programs-copy{left:34px;top:266px;font-size:11px;line-height:14px;font-weight:500;color:var(--white)}
  .program{top:270px;display:flex;align-items:center;gap:8px;color:var(--white);font-size:10px;line-height:12px;font-weight:500}
  .program .ico{width:32px;height:32px;border-radius:50%;background:var(--navy-deep);display:flex;align-items:center;justify-content:center;flex:none}

  .contact-band{left:0;top:329px;width:745px;height:153px;background:linear-gradient(90deg,var(--green) 0%,var(--green) 52%,#d7eaa9 72%,#ffffff 92%)}
  .contact-label{left:49px;top:357px;font-size:14px;color:var(--navy)}
  .contact-name{left:46px;top:376px;font-size:20px;font-weight:600;color:var(--navy)}
  .contact-phone{left:45px;top:401px;font-size:28px;font-weight:600;color:var(--navy);letter-spacing:-.3px}
  .contact-email{left:47px;top:438px;font-size:15px;font-weight:500;color:var(--navy)}
  .portrait{left:306px;top:333px;width:145px;height:149px;background:linear-gradient(180deg,#2a2a2a 0%,#1b1b1b 40%,#111 100%)}
  .brand-back{left:530px;top:373px;width:165px;text-align:center;font-size:17px;line-height:20px;font-weight:700;color:var(--navy)}
  .nmls-back{left:530px;top:451px;width:152px;text-align:center;font-size:13.5px;font-weight:500;color:var(--navy)}
</style>
</head>
<body>

<section class="card card--front" aria-label="Postcard front">
  <div class="abs front-haze" role="img" aria-label="Faded city skyline in light grey"></div>
  <h1 class="abs headline">IS A PROPERTY LIEN<br>PUTTING YOUR HOME <span class="accent">AT RISK?</span></h1>
  <p class="abs lien-types">HOA Liens • Tax Liens • Municipal Charges • Other Property-Related Liens</p>
  <div class="abs rule"></div>
  <p class="abs options">You may have options to resolve outstanding<br>liens and protect your home.</p>

  <div class="abs brand-front">Bluegate Lending<br>Partners, Inc.</div>

  <div class="abs green-band"></div>
  <p class="abs help-title">A Refinance or Home Equity Line<br>of Credit (HELOC) may help you:</p>
  <ul class="abs help-list">
    <li>Pay off qualifying liens</li>
    <li>Access your home's equity</li>
    <li>Consolidate debt into one<br>manageable payment</li>
    <li>Improve your financial flexibility</li>
    <li>Avoid additional penalties, fees,<br>or collection actions</li>
  </ul>

  <div class="abs urgent-circle">Don't wait<br>until the<br>situation<br>becomes<br>more difficult.</div>

  <div class="abs call-band" role="img" aria-label="Blue band fading into a dark city skyline"></div>
  <div class="abs photo-circle" role="img" aria-label="Photo of a worried couple reviewing bills at a coffee table"></div>

  <p class="abs call-text"><b>Call today</b> for a confidential<br>review of your options.</p>
  <div class="abs contact-row">
    <span class="phone-big">
      <svg width="9" height="16" viewBox="0 0 9 16" aria-hidden="true"><path d="M6 1 3 1C1.5 3 1 5.5 1 8s.5 5 2 7h3l1-3-2.3-1C4.3 9.5 4.3 6.5 4.7 5L7 4z" fill="#fff"/></svg>
      (800) 647-2915 x 42
    </span>
    <span class="web">
      <svg width="11" height="11" viewBox="0 0 12 12" aria-hidden="true"><g fill="none" stroke="#fff" stroke-width="1"><circle cx="6" cy="6" r="5"/><ellipse cx="6" cy="6" rx="2.2" ry="5"/><path d="M1 6h10M2 3.3h8M2 8.7h8"/></g></svg>
      www.bluegatelendco.com
    </span>
  </div>
  <p class="abs nmls-front">NMLS #381640</p>
</section>

<section class="card card--back" aria-label="Postcard back">
  <div class="abs back-haze" role="img" aria-label="Faded grey city skyline"></div>
  <h2 class="abs back-headline">YOUR HOME EQUITY<br>COULD BE THE SOLUTION</h2>
  <p class="abs notice-lead">If you have received notices regarding:</p>
  <ul class="abs notice-list">
    <li>Delinquent Property Taxes</li>
    <li>HOA or Condo Association Assessments</li>
    <li>Municipal Utility Liens</li>
    <li>Special Assessments</li>
    <li>Other Property-Related Obligations</li>
  </ul>
  <p class="abs qualify">You may qualify for financing options designed to help<br>satisfy those obligations and bring your property current.</p>
  <div class="abs stamp-box" aria-label="Postage area"></div>

  <div class="abs programs-band"></div>
  <svg class="abs programs-intro" viewBox="0 0 285 79" aria-hidden="true"><path d="M0 0H255C268 22 283 45 285 79H0Z" fill="#0e4c83"/></svg>
  <p class="abs programs-copy">Our experienced mortgage professionals<br>can review your situation and discuss<br>available programs, including:</p>

  <div class="abs program" style="left:292px">
    <span class="ico"><svg width="18" height="12" viewBox="0 0 18 12" aria-hidden="true"><g fill="none" stroke="#fff" stroke-width="1"><rect x=".5" y=".5" width="17" height="11"/><rect x="2.5" y="2.5" width="13" height="7"/><circle cx="9" cy="6" r="2.2"/></g></svg></span>
    <span>Cash-Out<br>Refinancing</span>
  </div>
  <div class="abs program" style="left:406px;top:265px">
    <span class="ico"><svg width="16" height="16" viewBox="0 0 16 16" aria-hidden="true"><g fill="none" stroke="#fff" stroke-width="1"><path d="M1 8 8 1.5 15 8M3 6.5V15h10V6.5"/><circle cx="8" cy="10" r="2.5"/></g></svg></span>
    <span>Home Equity<br>Lines of Credit<br>(HELOCs)</span>
  </div>
  <div class="abs program" style="left:532px;top:265px">
    <span class="ico"><svg width="18" height="16" viewBox="0 0 18 16" aria-hidden="true"><g fill="none" stroke="#fff" stroke-width="1"><path d="M3 7 9 2l6 5M5 6v4h8V6"/><path d="M1 12h5l3 2h6l2-2"/></g></svg></span>
    <span>Home<br>Equity<br>Loans</span>
  </div>
  <div class="abs program" style="left:614px;top:265px">
    <span class="ico"><svg width="16" height="16" viewBox="0 0 16 16" aria-hidden="true"><g fill="none" stroke="#fff" stroke-width="1"><rect x="2" y="1.5" width="9" height="13"/><path d="M4 4.5h5M4 7h5M4 9.5h3"/><circle cx="12.5" cy="11.5" r="2.5"/></g></svg></span>
    <span>Debt<br>Consolidation<br>Solution</span>
  </div>

  <div class="abs contact-band"></div>
  <p class="abs contact-label">CONTACT</p>
  <p class="abs contact-name">MARCUS DELANEY</p>
  <p class="abs contact-phone">(800) 647-2915 x42</p>
  <p class="abs contact-email">mdelaney@bluegatelendco.com</p>
  <div class="abs portrait" role="img" aria-label="Portrait of the loan officer in a dark hat and jacket"></div>
  <div class="abs brand-back">Bluegate Lending<br>Partners, Inc.</div>
  <p class="abs nmls-back">NMLS #57308</p>
</section>

</body>
</html>
```